Bright Loom Allies, LLC
Collaborative Contract Solutions
Modern
Owen Darby
Managing Director
12 Juniper Vale Road
Suite 240
Danvers, MA 01847
owen@brightloomallies.com
www.brightloomallies.com
Docs said to upload this logo format.

```html
<!DOCTYPE html>
<html lang="en">
<head>
<meta charset="utf-8">
<title>Bright Loom Allies — Business Cards</title>
<link href="https://fonts.googleapis.com/css2?family=Open+Sans:wght@400;600;700&display=swap" rel="stylesheet">
<style>
  :root {
    --bg: #e9e6e1;
    --card-white: #ffffff;
    --brand-blue: #1a63b0;
    --blue-dark: #0e4f97;
    --blue-mid: #2a7cc9;
    --blue-light: #5aa5e3;
    --ink-grey: #8a8d91;
    --rule: #c9d3de;
    --text-light: #ffffff;
    --text-soft: #dceaf8;
  }
  * { margin: 0; padding: 0; box-sizing: border-box; }
  html, body {
    width: 1200px; height: 785px; overflow: hidden;
    background: var(--bg);
    font-family: "Open Sans", Arial, sans-serif;
  }
  .canvas { position: relative; width: 1200px; height: 785px; }
  .card {
    position: absolute;
    border-radius: 16px;
    overflow: hidden;
    box-shadow: 0 6px 18px rgba(0,0,0,0.18);
  }

  /* Front card */
  .card-front { left: 154px; top: 120px; width: 448px; height: 271px; background: var(--card-white); }
  .front-brand {
    position: absolute; top: 40px; left: 0; width: 100%;
    display: flex; flex-direction: column; align-items: center; gap: 8px;
  }
  .brand-dot { width: 34px; height: 34px; border-radius: 50%; background: var(--brand-blue); }
  .brand-name { font-weight: 600; color: var(--brand-blue); font-size: 24px; letter-spacing: -0.2px; }
  .front-rule { position: absolute; top: 148px; left: 0; width: 100%; height: 2px; background: var(--rule); }
  .front-band {
    position: absolute; top: 162px; left: 0; width: 100%; height: 109px;
    background: linear-gradient(180deg, var(--blue-mid) 0%, var(--blue-dark) 100%);
  }
  .front-band::before {
    content: ""; position: absolute; top: 0; left: 0; width: 100%; height: 14px;
    background: linear-gradient(90deg, rgba(255,255,255,0.25), rgba(255,255,255,0.05));
  }
  .person { position: absolute; left: 10px; top: 20px; color: var(--text-light); }
  .person-name { font-size: 17px; font-weight: 700; }
  .person-title { font-size: 10px; color: var(--text-soft); }
  .contact {
    position: absolute; left: 245px; top: 8px; color: var(--text-light);
    font-size: 9.5px; line-height: 13px; list-style: none;
  }
  .contact li { display: flex; align-items: center; gap: 5px; }
  .contact svg { width: 9px; height: 9px; fill: var(--text-light); flex: none; }

  /* Blue back card */
  .card-back-blue {
    left: 631px; top: 120px; width: 475px; height: 271px;
    background: radial-gradient(ellipse at 45% 40%, var(--blue-light) 0%, var(--blue-mid) 45%, var(--blue-dark) 100%);
  }
  .back-brand {
    position: absolute; left: 0; width: 100%;
    display: flex; align-items: center; justify-content: center; gap: 10px;
  }
  .card-back-blue .back-brand { top: 105px; }
  .card-back-blue .brand-name { color: var(--text-light); }
  .card-back-blue .brand-dot { background: var(--text-light); width: 26px; height: 26px; }
  .back-url { position: absolute; bottom: 18px; left: 0; width: 100%; text-align: center; font-size: 10px; }
  .card-back-blue .back-url { color: var(--text-light); }

  /* White back card */
  .card-back-white { left: 374px; top: 434px; width: 473px; height: 276px; background: var(--card-white); }
  .card-back-white .back-brand { top: 112px; }
  .card-back-white .brand-dot { width: 26px; height: 26px; }
  .card-back-white .back-url { color: var(--ink-grey); bottom: 22px; }
</style>
</head>
<body>
<main class="canvas">

  <section class="card card-front" aria-label="Business card front">
    <div class="front-brand">
      <span class="brand-dot"></span>
      <span class="brand-name">Bright Loom Allies</span>
    </div>
    <div class="front-rule"></div>
    <div class="front-band">
      <div class="person">
        <p class="person-name">Owen Darby</p>
        <p class="person-title">Managing Director</p>
      </div>
      <ul class="contact">
        <li>12 Juniper Vale Road</li>
        <li>Suite 240</li>
        <li>Danvers, MA 01847</li>
        <li><svg viewBox="0 0 10 10"><path d="M2 0h2l1 3-1.5 1a6 6 0 0 0 2.5 2.5L7 5l3 1v2a2 2 0 0 1-2 2A8 8 0 0 1 0 2a2 2 0 0 1 2-2z"/></svg>978.555.0142</li>
        <li><svg viewBox="0 0 10 10"><rect x="0" y="3" width="10" height="6" rx="1"/><rect x="2" y="0" width="6" height="3"/></svg>978.555.0187</li>
        <li><svg viewBox="0 0 10 10"><circle cx="5" cy="5" r="5"/></svg>owen@brightloomallies.com</li>
        <li><svg viewBox="0 0 10 10"><circle cx="5" cy="5" r="5"/></svg>www.brightloomallies.com</li>
      </ul>
    </div>
  </section>

  <section class="card card-back-blue" aria-label="Business card back, blue">
    <div class="back-brand">
      <span class="brand-dot"></span>
      <span class="brand-name">Bright Loom Allies</span>
    </div>
    <p class="back-url">www.brightloomallies.com</p>
  </section>

  <section class="card card-back-white" aria-label="Business card back, white">
    <div class="back-brand">
      <span class="brand-dot"></span>
      <span class="brand-name">Bright Loom Allies</span>
    </div>
    <p class="back-url">www.brightloomallies.com</p>
  </section>

</main>
</body>
</html>
```